Business Card - The Harborline Group

We need a business card for a new venture capital fund and innovation accelerator based in San Francisco, CA. The Harborline Group will back, fund and scale life-transforming businesses. We intend to provide capital along with strategic and tactical direction to teams running exponential organizations. We are backing great ideas for vast markets with passionate visionaries. We facilitate the rapid creation of life-transforming businesses, help invent or re-invent critical industries and move the frontier of progress for the good of humankind. Maplecrest University defines Exponential Organizations as those whose impact (cost reduction or output) is disproportionally large – at least 10x larger – compared to its peers because of the use of new organizational techniques that leverage accelerating technologies. ExOs are characterized by a massive transformative purpose (MTP), a skunkworks organization and passionate teams of brilliant mountain-climbers with technical backgrounds.

Industry/Entity Type

Business

Contact Information for Business Card

Peter Odell
Managing Director

peter@theharborlinegroup.com
+1.628.307.4190

Font styles to use
Sans Serif

Requirements
Must have
• - logo
• - website: www.theharborlinegroup.com

```html
<!DOCTYPE html>
<html lang="en">
<head>
<meta charset="utf-8">
<title>The Harborline Group – Business Card</title>
<link rel="stylesheet" href="https://fonts.googleapis.com/css2?family=Roboto+Condensed:wght@400;700&display=swap">
<style>
  :root {
    --card-bg: #f2f2f2;
    --pattern-light: #f6f6f6;
    --pattern-dark: #e4e4e4;
    --ink: #3e3e3e;
    --ink-soft: #9b9b9b;
    --accent-blue: #2f6db3;
    --rule: #6a6a6a;
  }
  * { margin: 0; padding: 0; box-sizing: border-box; }
  html, body {
    width: 686px;
    height: 1200px;
    overflow: hidden;
    background: var(--card-bg);
  }
  .card {
    position: relative;
    width: 686px;
    height: 1200px;
    overflow: hidden;
    background: var(--card-bg);
    font-family: "Roboto Condensed", "Arial Narrow", sans-serif;
    color: var(--ink);
  }
  .background-pattern {
    position: absolute;
    inset: 0;
    background: linear-gradient(160deg, var(--pattern-light) 0%, var(--pattern-dark) 55%, var(--pattern-light) 100%);
  }
  .brand {
    position: absolute;
    top: 92px;
    left: 52px;
    width: 590px;
    display: flex;
    align-items: flex-start;
    gap: 34px;
  }
  .brand-mark {
    flex: 0 0 auto;
    width: 120px;
    height: 120px;
    margin-top: 26px;
    border-radius: 50%;
    background: var(--accent-blue);
  }
  .brand-text { flex: 1; }
  .brand-name {
    font-weight: 700;
    font-size: 54px;
    line-height: 1.02;
    letter-spacing: 1px;
    text-transform: uppercase;
    color: var(--ink);
  }
  .brand-rule {
    height: 2px;
    background: var(--rule);
    margin: 14px 0 12px;
  }
  .brand-tagline {
    font-weight: 400;
    font-size: 20px;
    line-height: 1.2;
    letter-spacing: 0.3px;
    text-transform: uppercase;
    color: var(--ink);
  }
  .person {
    position: absolute;
    top: 572px;
    left: 0;
    width: 100%;
    text-align: center;
  }
  .person-name {
    font-weight: 700;
    font-size: 40px;
    letter-spacing: 1.5px;
    text-transform: uppercase;
    color: var(--ink);
  }
  .person-title {
    margin-top: 6px;
    font-weight: 400;
    font-size: 25px;
    letter-spacing: 0.5px;
    text-transform: uppercase;
    color: var(--ink-soft);
  }
  .contact {
    position: absolute;
    top: 1030px;
    left: 0;
    width: 100%;
    text-align: center;
  }
  .contact-phone {
    font-weight: 700;
    font-size: 62px;
    letter-spacing: 1px;
    line-height: 1;
    color: var(--ink);
  }
  .contact-web {
    margin-top: 22px;
    font-weight: 700;
    font-size: 27px;
    letter-spacing: 0.5px;
    text-transform: uppercase;
    color: #1e1e1e;
  }
</style>
</head>
<body>
  <main class="card">
    <div class="background-pattern" role="img" aria-label="Faint light grey hexagon pattern across the card background"></div>

    <header class="brand">
      <div class="brand-mark"></div>
      <div class="brand-text">
        <h1 class="brand-name">The Harborline<br>Group</h1>
        <div class="brand-rule"></div>
        <p class="brand-tagline">Venture fund and innovation accelerator<br>for exponential technologies</p>
      </div>
    </header>

    <section class="person">
      <h2 class="person-name">Peter Odell</h2>
      <p class="person-title">Managing Director</p>
    </section>

    <footer class="contact">
      <p class="contact-phone">1-628-307-4190</p>
      <p class="contact-web">www.theharborlinegroup.com</p>
    </footer>
  </main>
</body>
</html>
```